Stationary and document suite for consultancy business in Australia called Lumara

I would like to get a suite of documents suitable for my new business called Lumara. I have included the original brief below, however have already selected a design for the logo. I would like to get:
Letter head - simple letter template with "V" logo embossed in background
Word document - standard format with "V" logo embossed in background
Proposal document - bolder pages with cover and back cover, include empty pages with footer as well as contents
Powerpoint presentation - open to ideas
Email signature - banner style or text, open to ideas
Brief that was given for logo (logo not required)
The name of the business is derived from the latin word for green ("Viridis") combined with "co" which is intended to represent a number of different words: collaborative, cooperative, coaching, collective,  construction, consulting, etc.
My objective for the brand is to represent a dynamic, progressive and collaborative business, where our people have fun and enjoy their work.
The objective of our business is to provide consultancy services to construction businesses, mainly aimed at building high performing teams and strategic growth. We will create learning and development tools that businesses can use to increase staff satisfaction and retention. Our future goal is to invest in decarbonisation and sustainability technology for use in the construction industry.
Our target market is construction business leaders and infrastructure owners, who operate road, rail and utility assets. We also want to present as a dynamic, progressive and fun place to work that will be attractive to new employees.

```html
<!DOCTYPE html>
<html lang="en">
<head>
<meta charset="utf-8">
<title>Lumara Stationery and Document Suite</title>
<link rel="stylesheet" href="https://fonts.googleapis.com/css2?family=Roboto:ital,wght@0,300;0,400;0,500;0,700;1,400&family=Montserrat:wght@700;800&display=swap">
<style>
:root{
  --board:#d1d1d1;
  --paper:#ffffff;
  --dark:#444446;
  --green:#8cc63f;
  --grey:#6d6e71;
  --text:#555557;
  --photo:#4a4a4c;
  --placeholder:#acacac;
  --cover-tint:#f2f5fc;
}
*{box-sizing:border-box;margin:0;padding:0}
html,body{width:791px;height:1200px;overflow:hidden}
body{background:var(--board);font-family:"Roboto",sans-serif;color:var(--text);position:relative}
.sheet{position:absolute;background:var(--paper);overflow:hidden}
.label{position:absolute;font-size:4.6px;letter-spacing:.04em;color:#333;text-align:center;text-transform:uppercase}
.brand{position:absolute;font-family:"Roboto",sans-serif;font-weight:400;color:var(--grey);letter-spacing:.03em;line-height:1;white-space:nowrap}
.band{position:absolute;left:0;right:0;bottom:0;height:4px;background:linear-gradient(110deg,var(--dark) 78%,#fff 78% 79%,var(--green) 79%)}
.contact{position:absolute;list-style:none;font-size:3.4px;line-height:4.2px;color:var(--text)}
.contact li{display:flex;align-items:center;gap:2px}
.contact .ic{width:2.4px;height:2.4px;border-radius:50%;background:var(--green);flex:none}
.contact.right li{justify-content:flex-end}
.contact.light{color:#fff}
.tiny{font-size:3px;line-height:4px;color:var(--text)}

/* proposal */
.cover-front{background:var(--cover-tint);text-align:center}
.cover-front .year{position:absolute;top:90px;left:0;right:0;font-family:"Montserrat",sans-serif;font-weight:800;font-size:22px;color:var(--green)}
.cover-front .title{position:absolute;top:112px;left:0;right:0;font-family:"Montserrat",sans-serif;font-weight:800;font-size:21px;line-height:22px;letter-spacing:.14em;color:var(--grey)}
.cover-front .prep{position:absolute;top:168px;left:0;right:0;font-size:5.4px;font-weight:500;color:var(--green)}
.cover-front .name{position:absolute;top:177px;left:0;right:0;font-size:9px;font-weight:500;color:var(--dark)}
.cover-front .role{position:absolute;top:187px;left:0;right:0;font-size:4.2px;font-style:italic;color:var(--text)}
.cover-front .date{position:absolute;top:200px;left:0;right:0;font-size:5.6px;color:var(--text)}
.cover-front .blurb{position:absolute;top:229px;left:16px;right:16px;font-size:3.8px;line-height:5px;font-style:italic;color:var(--text)}
.cover-back{background:var(--dark)}
.cover-back .thanks{position:absolute;right:24px;top:206px;font-size:10.5px;font-weight:700;color:var(--green)}
.doc-head{position:absolute;left:16px;top:17px;font-size:8px;font-weight:700;color:var(--dark);letter-spacing:.02em}
.doc-head span{color:var(--green)}
.doc-rule{position:absolute;left:16px;right:18px;height:.6px;background:var(--green)}
.doc-photo{position:absolute;left:16px;top:40px;width:147px;height:97px;background:var(--placeholder)}
.doc-body{position:absolute;left:16px;width:147px;top:142px;font-size:3.2px;line-height:4.6px;color:var(--text);text-align:justify}
.doc-body p{margin-bottom:4px}
.doc-foot{position:absolute;left:16px;right:18px;top:236px;display:flex;justify-content:space-between;font-size:3.8px;color:var(--dark)}

/* slides */
.slide{width:185px;height:138px}
.slide.dark{background:var(--dark)}
.slide.pale{background:linear-gradient(180deg,#ffffff 0%,#dadada 100%)}
.title-block{position:absolute;right:18px;top:89px;text-align:right;line-height:1}
.title-block .welcome{font-size:8.4px;font-weight:700;color:var(--green)}
.title-block .deck{font-size:8.4px;font-weight:500;color:var(--dark);margin-top:.5px}
.slide.dark .title-block .deck{color:#fff}
.title-block .desc{font-size:6.2px;font-style:italic;color:var(--green);margin-top:.5px}
.slide-title{position:absolute;left:10px;top:11px;font-size:8.6px;font-weight:700;color:var(--green);line-height:1}
.slide-sub{position:absolute;left:10px;top:20px;font-size:4.4px;color:var(--dark);line-height:1}
.slide-rule{position:absolute;left:40px;right:38px;top:24px;height:.5px;background:var(--dark)}
.slide-foot{position:absolute;left:10px;right:10px;top:122px;border-top:.6px solid var(--green);display:flex;justify-content:space-between;padding-top:2.5px;font-size:3.6px;color:var(--dark)}
.slide-foot b{font-weight:700}
.toc{position:absolute;left:15px;right:15px;top:37px;list-style:none}
.toc li{display:flex;align-items:flex-end;gap:2px;height:15.5px;font-size:4.8px;color:var(--dark)}
.toc .lead{flex:1;border-bottom:.4px dotted #999;margin-bottom:1px}
.toc .pg{font-size:3px}
.team{position:absolute;top:33px;width:38px}
.team .photo{width:36px;height:36px;background:var(--photo);border:1.5px solid #fff;box-shadow:0 .5px 1.5px rgba(0,0,0,.45);color:#ddd;font-size:4.4px;display:flex;align-items:center;justify-content:center}
.team .who{font-size:3.6px;color:var(--green);margin-top:3px}
.team .tiny{font-size:2.5px;line-height:3.3px}
.bullets{position:absolute;left:10px;right:12px;top:37px;list-style:none}
.bullets li{position:relative;padding-left:6px;font-size:2.8px;line-height:3.9px;margin-bottom:5px}
.bullets li::before{content:"";position:absolute;left:1px;top:1px;width:1.8px;height:1.8px;border-radius:50%;background:var(--green)}
.services{position:absolute;left:19px;right:20px;top:34px;list-style:none}
.services li{font-size:2.8px;line-height:3.9px;margin-bottom:4.4px}
.thanks-big{position:absolute;right:20px;top:72px;text-align:right;line-height:1}
.thanks-big .t1{font-size:17px;font-weight:300;color:var(--green)}
.thanks-big .t2{font-size:11px;font-weight:300;color:#fff}

/* signatures */
.sig-name{position:absolute;font-size:5.4px;font-weight:500;color:var(--grey);letter-spacing:.02em}
.sig-role{position:absolute;font-size:4.2px;color:var(--green)}
</style>
</head>
<body>

<!-- Letterhead -->
<section class="sheet" style="left:46px;top:49px;width:180px;height:233px">
  <div class="brand" style="left:14px;top:14px;font-size:12px">Lumara</div>
  <ul class="contact" style="left:128px;top:16px">
    <li><i class="ic"></i>+61 412 508 930</li>
    <li><i class="ic"></i>reid@lumara.com.au</li>
    <li><i class="ic"></i>lumara.com.au</li>
  </ul>
  <div class="band"></div>
</section>
<p class="label" style="left:46px;top:294px;width:180px">Letter head</p>

<!-- Word document -->
<section class="sheet" style="left:243px;top:49px;width:180px;height:233px">
  <div class="brand" style="left:13px;top:14px;font-size:12px">Lumara</div>
  <ul class="contact" style="left:128px;top:15px">
    <li><i class="ic"></i>+61 412 508 930</li>
    <li><i class="ic"></i>reid@lumara.com.au</li>
    <li><i class="ic"></i>lumara.com.au</li>
  </ul>
  <div class="band"></div>
</section>
<p class="label" style="left:243px;top:294px;width:180px">Word document</p>

<!-- Word document third page -->
<section class="sheet" style="left:439px;top:49px;width:180px;height:233px">
  <div class="brand" style="left:13px;top:15px;font-size:7px">Lumara</div>
  <div class="band"></div>
</section>
<p class="label" style="left:439px;top:294px;width:180px">Word document third page</p>

<!-- Envelope back -->
<section class="sheet" style="left:585px;top:111px;width:181px;height:82px">
  <div style="position:absolute;left:3px;right:3px;top:0;height:26px;background:var(--dark);border-radius:0 0 13px 13px"></div>
  <div class="brand" style="left:77px;top:9px;font-size:7px;color:#fff">Lumara</div>
</section>
<!-- Envelope front -->
<section class="sheet" style="left:568px;top:176px;width:182px;height:83px;box-shadow:0 0 1px rgba(0,0,0,.15)">
  <div class="brand" style="left:11px;top:10px;font-size:11px">Lumara</div>
  <div class="band" style="height:3.5px"></div>
</section>
<p class="label" style="left:585px;top:265px;width:181px">Envelope front &amp; back</p>

<!-- Proposal front -->
<section class="sheet cover-front" style="left:46px;top:316px;width:179px;height:254px">
  <div class="brand" style="left:0;right:0;top:34px;font-size:33px;text-align:center">Lumara</div>
  <div class="year">2022</div>
  <div class="title">ANNUAL<br>REPORT</div>
  <div class="prep">PREPARED BY</div>
  <div class="name">ALEX MARLOW</div>
  <div class="role">Managing Director</div>
  <div class="date">15, JUNE, 2022</div>
  <p class="blurb">Strategy, people and growth for the construction sector, delivered with care and a clear plan for every project.</p>
  <div class="band"></div>
</section>
<p class="label" style="left:46px;top:581px;width:165px">Proposal front</p>

<!-- Proposal back -->
<section class="sheet cover-back" style="left:242px;top:316px;width:179px;height:254px">
  <div class="thanks">Thank You</div>
  <ul class="contact light right" style="right:24px;top:221px">
    <li>+61 412 508 930<i class="ic"></i></li>
    <li>reid@lumara.com.au<i class="ic"></i></li>
    <li>lumara.com.au<i class="ic"></i></li>
  </ul>
</section>
<p class="label" style="left:242px;top:581px;width:165px">Proposal back</p>

<!-- Proposal inner -->
<section class="sheet" style="left:440px;top:316px;width:179px;height:254px">
  <h2 class="doc-head">ABOUT <span>US</span></h2>
  <div class="brand" style="right:18px;top:16px;font-size:8px">Lumara</div>
  <div class="doc-rule" style="top:28px"></div>
  <div class="doc-photo" role="img" aria-label="Photo of the team at work"></div>
  <div class="doc-body">
    <p>We help construction leaders build strong teams and plan steady growth. Our work starts with listening, then moves to clear tools that people can use every day on site and in the office. We measure what matters and share results openly.</p>
    <p>Our programs cover coaching, team health checks and leadership training. Each one is shaped around the client, the site and the crew. We work with road, rail and utility owners to lift staff satisfaction and keep good people for longer. Over time we plan to back cleaner building methods and lower carbon materials across the industry.</p>
    <p>Talk to us about your next project and we will map a simple path forward.</p>
  </div>
  <div class="doc-rule" style="top:234px;height:.4px"></div>
  <div class="doc-foot"><span>LUMARA.COM.AU</span><span>1</span></div>
</section>
<p class="label" style="left:440px;top:580px;width:165px">Proposal inner</p>

<!-- Slide: title dark -->
<section class="sheet slide dark" style="left:34px;top:610px">
  <div class="brand" style="right:18px;top:70px;font-size:15px;color:#fff">Lumara</div>
  <div class="title-block">
    <div class="welcome">Welcome to Our</div>
    <div class="deck">PRESENTATION NAME</div>
    <div class="desc">Description</div>
  </div>
</section>

<!-- Slide: title light -->
<section class="sheet slide pale" style="left:230px;top:610px">
  <div class="brand" style="right:18px;top:70px;font-size:15px">Lumara</div>
  <div class="title-block">
    <div class="welcome">Welcome to Our</div>
    <div class="deck" style="color:var(--grey)">PRESENTATION NAME</div>
    <div class="desc">Description</div>
  </div>
</section>

<!-- Slide: contents -->
<section class="sheet slide" style="left:426px;top:610px">
  <h3 class="slide-title">CONTENTS</h3>
  <p class="slide-sub">Sub Heading</p>
  <div class="slide-rule"></div>
  <div class="brand" style="right:10px;top:19px;font-size:8px">Lumara</div>
  <ol class="toc">
    <li>I&nbsp; ABOUT US<span class="lead"></span><span class="pg">2</span></li>
    <li>II&nbsp; OUR SERVICES<span class="lead"></span><span class="pg">3</span></li>
    <li>III&nbsp; CASE STUDY<span class="lead"></span><span class="pg">4</span></li>
    <li>IV&nbsp; DIAGRAM<span class="lead"></span><span class="pg">5</span></li>
    <li>V&nbsp; CONTACUS<span class="lead"></span><span class="pg">6</span></li>
  </ol>
  <div class="slide-foot"><span>www.<b>lumara</b>.com.au</span><span>PAGE1</span></div>
</section>

<!-- Slide: about us -->
<section class="sheet slide" style="left:34px;top:766px">
  <h3 class="slide-title">ABOUT US</h3>
  <p class="slide-sub">Sub Heading</p>
  <div class="slide-rule"></div>
  <div class="brand" style="right:10px;top:19px;font-size:8px">Lumara</div>
  <div class="team" style="left:17px">
    <div class="photo" role="img" aria-label="Team member portrait">Photo</div>
    <p class="who">Mr Nobody</p>
    <p class="tiny">Project lead</p>
    <p class="tiny" style="margin-top:2px">Team lead with ten years on major road and rail projects.</p>
  </div>
  <div class="team" style="left:71px">
    <div class="photo" role="img" aria-label="Team member portrait">Photo</div>
    <p class="who">Mr Nobody</p>
    <p class="tiny">Project lead</p>
    <p class="tiny" style="margin-top:2px">Team lead with ten years on major road and rail projects.</p>
  </div>
  <div class="team" style="left:127px">
    <div class="photo" role="img" aria-label="Team member portrait">Photo</div>
    <p class="who">Mr Nobody</p>
    <p class="tiny">Project lead</p>
    <p class="tiny" style="margin-top:2px">Team lead with ten years on major road and rail projects.</p>
  </div>
  <div class="slide-foot"><span>www.<b>lumara</b>.com.au</span><span>PAGE1</span></div>
</section>

<!-- Slide: bullet text -->
<section class="sheet slide" style="left:230px;top:766px">
  <h3 class="slide-title">BULLET TEXT</h3>
  <p class="slide-sub">Sub Heading</p>
  <div class="slide-rule"></div>
  <div class="brand" style="right:10px;top:19px;font-size:8px">Lumara</div>
  <ul class="bullets">
    <li>Clear goals help every crew member see how daily work links to the bigger picture.</li>
    <li>Regular check-ins keep teams on track and surface small issues before they grow into big ones.</li>
    <li>Training tools are built for site life, short, practical and easy to pick up between tasks.</li>
    <li>Good leaders listen first, then act, and they give credit to the people who did the work.</li>
    <li>Retention grows when staff feel valued, trusted and able to learn new skills on the job.</li>
  </ul>
  <div class="slide-foot"><span>www.<b>lumara</b>.com.au</span><span>PAGE1</span></div>
</section>

<!-- Slide: case study -->
<section class="sheet slide" style="left:426px;top:766px">
  <h3 class="slide-title">CASE STUDY</h3>
  <p class="slide-sub">Sub Heading</p>
  <div class="slide-rule"></div>
  <div class="brand" style="right:10px;top:19px;font-size:8px">Lumara</div>
  <svg style="position:absolute;left:26px;top:32px" width="66" height="60" viewBox="0 0 66 60" role="img" aria-label="Bar chart of four results">
    <g stroke="#cfcfcf" stroke-width=".35">
      <line x1="0" y1="2" x2="66" y2="2"/><line x1="0" y1="10" x2="66" y2="10"/><line x1="0" y1="18" x2="66" y2="18"/>
      <line x1="0" y1="26" x2="66" y2="26"/><line x1="0" y1="34" x2="66" y2="34"/><line x1="0" y1="42" x2="66" y2="42"/>
      <line x1="0" y1="50" x2="66" y2="50"/><line x1="0" y1="58" x2="66" y2="58"/>
    </g>
    <g fill="#8cc63f">
      <rect x="10" y="4" width="8" height="54"/><rect x="18.5" y="11" width="8" height="47"/>
      <rect x="29" y="25" width="8" height="33"/><rect x="38" y="16" width="8" height="42"/>
    </g>
    <g fill="#fff" font-size="2.6" font-family="Roboto, sans-serif">
      <text transform="translate(15.5 57) rotate(-90)">Sub text1</text>
      <text transform="translate(24 57) rotate(-90)">Sub text2</text>
      <text transform="translate(34.5 57) rotate(-90)">Sub text3</text>
      <text transform="translate(43.5 57) rotate(-90)">Sub text4</text>
    </g>
  </svg>
  <p class="tiny" style="position:absolute;left:111px;top:35px;width:50px;font-size:2.6px;line-height:3.6px">Staff turnover fell by a third within the first year of the program. Site leads reported better morale and clearer communication across crews.</p>
  <p class="tiny" style="position:absolute;left:17px;right:12px;top:100px;font-size:2.6px;line-height:3.6px">A regional rail contractor worked with us for twelve months to rebuild team culture, set shared goals and train new supervisors across four sites.</p>
  <div class="slide-foot"><span>www.<b>lumara</b>.com.au</span><span>PAGE1</span></div>
</section>

<!-- Slide: diagram -->
<section class="sheet slide" style="left:34px;top:922px">
  <h3 class="slide-title">DIAGRAM</h3>
  <p class="slide-sub">Sub Heading</p>
  <div class="slide-rule"></div>
  <div class="brand" style="right:10px;top:19px;font-size:8px">Lumara</div>
  <p class="tiny" style="position:absolute;left:15px;top:40px;width:78px;text-align:center;font-size:2.7px;line-height:3.9px">Half of our work focuses on team health and leadership. The rest is split between growth planning and training tools that crews use on site every week.</p>
  <p class="tiny" style="position:absolute;left:15px;top:91px;width:78px;text-align:center;font-size:2.7px;line-height:3.9px">Numbers are drawn from the last twelve months of client projects.</p>
  <svg style="position:absolute;left:116px;top:33px" width="44" height="44" viewBox="-22 -22 44 44" role="img" aria-label="Pie chart of work split">
    <circle r="20" fill="#8cc63f"/>
    <path d="M0 0 L0 -20 A20 20 0 0 1 18.13 -8.45 Z" fill="#6d6e71" stroke="#fff" stroke-width=".6"/>
    <path d="M0 0 L19.70 3.47 A20 20 0 0 1 6.84 18.79 Z" fill="#6d6e71" stroke="#fff" stroke-width=".6"/>
    <path d="M0 0 L18.13 -8.45 A20 20 0 0 1 19.70 3.47 Z" fill="#8cc63f" stroke="#fff" stroke-width=".6"/>
  </svg>
  <div style="position:absolute;left:115px;top:86px;width:50px;font-size:2.5px;line-height:3.5px">
    <p style="display:flex;gap:2px;align-items:center"><i style="width:3px;height:3px;background:var(--green)"></i>Team health 50%</p>
    <p style="display:flex;gap:2px;align-items:center;border-top:.3px solid #ccc;border-bottom:.3px solid #ccc;margin-top:1px"><i style="width:3px;height:3px;background:var(--grey)"></i>Growth and training 50%</p>
    <p style="margin-top:4px">Based on client project hours.</p>
  </div>
  <div class="slide-foot"><span>www.<b>lumara</b>.com.au</span><span>PAGE1</span></div>
</section>

<!-- Slide: our services -->
<section class="sheet slide" style="left:230px;top:922px">
  <h3 class="slide-title">OUR SERVICES</h3>
  <p class="slide-sub">Sub Heading</p>
  <div class="slide-rule"></div>
  <div class="brand" style="right:10px;top:19px;font-size:8px">Lumara</div>
  <ol class="services">
    <li>1. Team coaching for site and office leaders.</li>
    <li>2. Health checks that show how a team really works.</li>
    <li>3. Growth plans built around clear, shared goals and simple steps.</li>
    <li>4. Leadership training for new supervisors and project managers across road and rail.</li>
    <li>5. Learning tools that staff can use on any device, any time, on site or at home.</li>
    <li>6. Support for cleaner building methods and lower carbon choices.</li>
  </ol>
  <div class="slide-foot"><span>www.<b>lumara</b>.com.au</span><span>PAGE1</span></div>
</section>

<!-- Slide: thanks -->
<section class="sheet slide dark" style="left:426px;top:922px">
  <div class="thanks-big">
    <div class="t1">Thanks</div>
    <div class="t2">For Coming</div>
  </div>
  <ul class="contact light right" style="right:24px;top:106px">
    <li>+61 412 508 930<i class="ic"></i></li>
    <li>reid@lumara.com.au<i class="ic"></i></li>
    <li>lumara.com.au<i class="ic"></i></li>
  </ul>
</section>

<!-- Email signature 01 -->
<section class="sheet" style="left:99px;top:1107px;width:180px;height:52px">
  <div class="brand" style="left:24px;top:14px;font-size:16px">Lumara</div>
  <p class="sig-name" style="left:100px;top:6px">REID CALLOWAY</p>
  <p class="sig-role" style="left:100px;top:12px">Director</p>
  <ul class="contact" style="left:100px;top:19px">
    <li><i class="ic"></i>+61 412 508 930</li>
    <li><i class="ic"></i>reid@lumara.com.au</li>
    <li><i class="ic"></i>lumara.com.au</li>
  </ul>
  <svg style="position:absolute;left:0;bottom:0" width="180" height="14" viewBox="0 0 180 14" preserveAspectRatio="none" aria-hidden="true">
    <path d="M0 3 Q90 10 180 4 L180 6 Q90 13 0 6 Z" fill="#8cc63f"/>
    <path d="M0 7 Q90 14 180 6 L180 14 L0 14 Z" fill="#444446"/>
  </svg>
</section>
<p class="label" style="left:99px;top:1165px;width:180px">Email signature 01</p>

<!-- Email signature 02 -->
<section class="sheet" style="left:353px;top:1110px;width:187px;height:41px">
  <div class="brand" style="left:12px;top:14px;font-size:11px">Lumara</div>
  <p class="sig-name" style="left:62px;top:14px">REID CALLOWAY</p>
  <p class="sig-role" style="left:79px;top:20px">Director</p>
  <ul class="contact" style="left:131px;top:13px">
    <li><i class="ic"></i>+61 412 508 930</li>
    <li><i class="ic"></i>reid@lumara.com.au</li>
    <li><i class="ic"></i>lumara.com.au</li>
  </ul>
</section>
<p class="label" style="left:353px;top:1168px;width:187px">Email signature 02</p>

</body>
</html>
```